Shipping cards

Expedited delivery of various business related products , packages ,parcels etc. Intrastate or Interstate.

Target Market(s)

business and or private customer base.with expedited needs and short term or long term needs.

Industry/Entity Type

Business

Contact Information for Business Card

would like the silhouette of my dog between the business name Amber{ } Fox . Amber Fox Freight ,Expedited Delivery, tel330-958-3637 fax TBD , dispatch@quillmail.test, Dennis J. Holt- Owner

Font styles to use
Serif

Requirements
Must have
• dog silhouette between Amber Fox or before and after name of company.
Should not have
• remove oval from silhouette around dog

```html
<!DOCTYPE html>
<html lang="en">
<head>
<meta charset="utf-8">
<title>Amber Fox Freight — Business Card</title>
<link href="https://fonts.googleapis.com/css2?family=Questrial&family=Open+Sans:wght@400;700&display=swap" rel="stylesheet">
<style>
  :root {
    --page: #e7e4df;
    --sky-light: #3fb8e6;
    --sky: #1e9fd8;
    --sky-deep: #0f7fb8;
    --ink: #0b0d10;
    --ink-soft: #1b1f24;
    --logo-ink: #0e1a22;
    --white: #f2f4f6;
  }
  html, body {
    margin: 0;
    width: 1200px;
    height: 1023px;
    overflow: hidden;
    background: var(--page);
  }
  .card {
    position: absolute;
    left: 150px;
    top: 254px;
    width: 900px;
    height: 514px;
    overflow: hidden;
    border-radius: 6px;
    box-shadow: 0 18px 40px rgba(0,0,0,.25);
    background: linear-gradient(180deg, var(--ink-soft), var(--ink) 60%);
  }
  .brand-panel {
    position: absolute;
    left: 0; top: 0;
    width: 100%; height: 232px;
    background: linear-gradient(100deg, var(--sky-deep) 0%, var(--sky) 45%, var(--sky-light) 100%);
  }
  .band-dark {
    position: absolute;
    left: 0; top: 232px;
    width: 100%; height: 34px;
    background: var(--ink);
  }
  .band-blue {
    position: absolute;
    left: 0; top: 266px;
    width: 100%; height: 26px;
    background: linear-gradient(90deg, var(--sky-deep), var(--sky-light));
  }
  .brand {
    position: absolute;
    left: 60px; top: 62px;
    font-family: "Questrial", sans-serif;
    color: var(--logo-ink);
  }
  .brand-name {
    font-size: 76px;
    line-height: 1;
    letter-spacing: 1px;
    margin: 0;
    font-weight: 400;
  }
  .brand-name .gap { display: inline-block; width: 44px; }
  .brand-tagline {
    margin: 14px 0 0 4px;
    font-size: 27px;
    letter-spacing: 1px;
  }
  .person {
    position: absolute;
    right: 44px; top: 316px;
    text-align: right;
    font-family: "Open Sans", sans-serif;
  }
  .person-name {
    margin: 0;
    font-size: 31px;
    font-weight: 700;
    letter-spacing: 1.5px;
    color: var(--sky);
  }
  .person-name .chev { margin: 0 10px; }
  .person-role {
    margin: 4px 60px 0 0;
    font-size: 19px;
    color: var(--white);
  }
  .contact {
    position: absolute;
    left: 56px; top: 372px;
    list-style: none;
    margin: 0; padding: 0;
    font-family: "Open Sans", sans-serif;
    font-size: 22px;
    color: var(--white);
  }
  .contact li {
    display: flex;
    align-items: center;
    height: 38px;
  }
  .contact svg {
    width: 22px; height: 22px;
    margin-right: 16px;
  }
</style>
</head>
<body>
  <section class="card" aria-label="Amber Fox Freight business card">
    <div class="brand-panel"></div>
    <div class="band-dark"></div>
    <div class="band-blue"></div>

    <div class="brand">
      <h1 class="brand-name">Amber<span class="gap"></span>Fox</h1>
      <p class="brand-tagline">Freight | Expedited Delivery</p>
    </div>

    <div class="person">
      <p class="person-name"><span class="chev">«</span>DENNIS J. HOLT<span class="chev">»</span></p>
      <p class="person-role">Owner</p>
    </div>

    <ul class="contact">
      <li>
        <svg viewBox="0 0 22 22" aria-hidden="true"><rect width="22" height="22" rx="3" fill="#1e9fd8"/><path d="M7 5h3l1 4-2 1.5a8 8 0 0 0 2.5 2.5L13 11l4 1v3c0 1-1 2-2 2A11 11 0 0 1 5 7c0-1 1-2 2-2z" fill="#0b0d10"/></svg>
        (412) 573-2916
      </li>
      <li>
        <svg viewBox="0 0 22 22" aria-hidden="true"><rect width="22" height="22" rx="3" fill="#1e9fd8"/><rect x="5" y="9" width="12" height="8" fill="#0b0d10"/><rect x="7" y="4" width="8" height="5" fill="#0b0d10"/></svg>
        (412) 573-2984
      </li>
      <li>
        <svg viewBox="0 0 22 22" aria-hidden="true"><rect width="22" height="22" rx="3" fill="#1e9fd8"/><rect x="4" y="6" width="14" height="10" fill="#0b0d10"/><path d="M4 6l7 6 7-6" stroke="#1e9fd8" stroke-width="1.5" fill="none"/></svg>
        dispatch@quillmail.test
      </li>
    </ul>
  </section>
</body>
</html>
```